Momentum Personal Training- Signage Design Project

Momentum Personal Training is looking for a signage design for our shop front windows and doors.

We have been in business for 12 years and are moving to a new and bigger premises for a fresh start, so we are feeling energetic, vibrant and excited.

We have 2 windows + 2 doors (photo included but taken at night so slightly dark)

The dimensions of each window are: 2100mm wide x 2660 height
The dimensions of each door is: 740mm wide x 1920mm height

IMPORTANT- If standing on sidewalk looking at the window signage, the right window needs to be partially blocked out. Not completely blocked out but allow an element of privacy for clients so that passers by would really need to concentrate to see in. Im open to suggestions on how this is done.

We also want to advertise our promo which is "$39 p.w Unlimited Personal Training* "

I would like that to stand out but can be on either window or wherever you think.

We would also like the website address potentially included somewhere www.fitlane-studio.com.au

I have made some notes below as to the kind of signage I think would look good, but im very open to suggestions.

It needs to look vibrant, possibly work in with our logo (attached) and most importantly it must catch the eye.

NOTE- Im open to suggestions and creative flare, im prepared to not necessarily make the logo a big part of the design so feel free to submit designs that dont rely on logo

About Us:

We are a personal training studio in Melbourne

We are somewhat unique for a PT studio in that we will have more equipment and better quality equipment than most of our competitors, but our prices are extremely affordable. Many studios that have these facilities will be charging much higher fees.

We are moving to a new area, for a fresh start and will be aggressively pushing to recruit as many clients as possible. There is a bigger competitor not far from us that has slightly better signage visibility, so we want to stand out.

75% of our clients are female, this tends to be the target demographic. We do however, want to be able to recruit male clients too, so we dont want our signage to suggest its a female gym.

We offer 1on1/Private personal training and small group/indoor bootcamp personal training. We specialise in both, but are probably angling more at the group training market as it offers a higher hourly wage to us + its cheaper for clients to afford.

Our client base is middle class, we dont tend to attract the upper class client.

We offer a very personable service where we know all our clients well and we build strong rapport with them.Our clients arent just number/members, we strive to get to know them personally and show we have a genuine interest in them.

Feel free to ask any questions, I will answer promptly as the deadline is near.

Target Market(s)

females aged 25-45. We wtill want to be able to attract male clients too. People who have been thinking about starting exercise

Industry/Entity Type

Training

Requirements
Must have
• * Should fit in with our logo colours i believe
* Signage must be warm and inviting. (Very important) We want women to be comfortable to come in, not too" hardcore". We do want to still be able to attract male clients too, so not so feminine that men wont feel comfortable.
*If standing on sidewalk looking at the window signage, the right window needs to be partially blocked out. Not completely blocked out but allow an element of privacy for clients so that passers by would really need to concentrate to see in. We also dont want people to feel like they are trapped in a dungeon with no outside light.
* Fresh, energetic
* Needs to catch the eye of motorists
* I dont want the design to look too busy with too much text (Very important)
* personable service where we know all our clients well and we build strong rapport with them.
Nice to have
• Im open to suggestions. I want it to stand out but not be trashy. I want motorists to remember us.
Should not have
• Dont want any designs that are too dark and overtly masculine
Nothing with too much text.
Passing motorist should be able to grasp the concept very quickly. Clear, not confusing.

```html
<!DOCTYPE html>
<html lang="en">
<head>
<meta charset="utf-8">
<title>Momentum Personal Training – Shopfront Signage</title>
<link rel="stylesheet" href="https://fonts.googleapis.com/css2?family=Arimo:wght@400;700&display=swap">
<style>
  :root {
    --page: #f4f4f4;
    --panel: #ffffff;
    --panel-edge: #8a8a8a;
    --teal-light: #4fc4d5;
    --teal-dark: #1c7a88;
    --band-rule: #111111;
    --charcoal: #3a3a3a;
    --ink: #333333;
    --white: #ffffff;
  }
  * { box-sizing: border-box; margin: 0; padding: 0; }
  html, body {
    width: 1200px; height: 1200px; overflow: hidden;
    background: var(--page);
    font-family: "Arimo", Arial, sans-serif;
  }
  .signage { position: relative; width: 1200px; height: 1200px; }
  .panel {
    position: absolute;
    background: var(--panel);
    border: 1px solid var(--panel-edge);
    overflow: hidden;
  }
  .panel--window-left  { left: 40px;  top: 345px; width: 402px; height: 510px; border-color: #222; }
  .panel--window-right { left: 753px; top: 345px; width: 405px; height: 510px; }
  .panel--header       { left: 452px; top: 345px; width: 294px; height: 103px; }
  .panel--door-left    { left: 452px; top: 457px; width: 142px; height: 399px; }
  .panel--door-right   { left: 600px; top: 457px; width: 144px; height: 399px; }

  .band {
    position: absolute; left: 0; right: 0; top: 180px; height: 194px;
    border-top: 3px solid var(--band-rule);
    border-bottom: 3px solid var(--band-rule);
    padding: 4px 0;
    background: var(--panel);
  }
  .band__fill {
    width: 100%; height: 100%;
    background: linear-gradient(to bottom, var(--teal-light), var(--teal-dark));
  }
  .slogan {
    position: absolute; left: 0; right: 0; top: 0;
    color: var(--white); font-size: 20px; line-height: 27px;
  }
  .slogan__line { position: absolute; white-space: nowrap; }
  .slogan__line--first  { left: 22px; top: 257px; }
  .slogan__line--second { right: 22px; top: 284px; }

  .brand {
    display: flex; align-items: center; justify-content: center; gap: 10px;
    height: 100%;
  }
  .brand__dot { width: 14px; height: 14px; border-radius: 50%; background: var(--teal-light); flex: none; }
  .brand__name { color: var(--ink); font-size: 19px; font-weight: 400; line-height: 1.15; }

  .door-box {
    position: absolute; left: 0; right: 0; top: 109px; height: 117px;
    background: var(--charcoal);
    display: flex; flex-direction: column; align-items: center; justify-content: center;
    color: var(--white); text-align: center;
  }
  .door-box__name { font-size: 20px; }
  .hours__title { font-size: 11px; margin-bottom: 3px; }
  .hours__line { font-size: 9.5px; line-height: 13px; }

  .promo {
    position: absolute; left: 47px; top: 89px; width: 330px; height: 330px;
    border-radius: 50%;
    border: 2px solid var(--band-rule);
    padding: 4px;
    background: var(--panel);
  }
  .promo__disc {
    width: 100%; height: 100%; border-radius: 50%;
    background: linear-gradient(to bottom, var(--teal-light), var(--teal-dark));
    color: var(--white); text-align: center;
    display: flex; flex-direction: column; align-items: center; justify-content: center;
  }
  .promo__price { font-size: 72px; font-weight: 700; line-height: 1; letter-spacing: -1px; }
  .promo__currency { font-size: 40px; vertical-align: 22px; margin-right: 2px; }
  .promo__offer { font-size: 20px; margin-top: 12px; }
  .promo__web { font-size: 14px; margin-top: 30px; }
</style>
</head>
<body>
<main class="signage">

  <section class="panel panel--window-left" aria-label="Left window">
    <div class="band"><div class="band__fill"></div></div>
    <p class="slogan">
      <span class="slogan__line slogan__line--first">Never get so busy making a living</span>
      <span class="slogan__line slogan__line--second">that you forget to make a life</span>
    </p>
  </section>

  <section class="panel panel--header" aria-label="Door header">
    <div class="brand">
      <span class="brand__dot"></span>
      <span class="brand__name">Momentum<br>Personal Training</span>
    </div>
  </section>

  <section class="panel panel--door-left" aria-label="Left door">
    <div class="door-box"><span class="door-box__name">Momentum</span></div>
  </section>

  <section class="panel panel--door-right" aria-label="Right door">
    <div class="door-box hours">
      <p class="hours__title">HOURS OF OPERATION</p>
      <p class="hours__line">Monday - Sunday</p>
      <p class="hours__line">HH:MM am - MM:MM pm</p>
    </div>
  </section>

  <section class="panel panel--window-right" aria-label="Right window">
    <div class="band"><div class="band__fill"></div></div>
    <div class="promo">
      <div class="promo__disc">
        <p class="promo__price"><span class="promo__currency">$</span>39 p.w</p>
        <p class="promo__offer">Unlimited Personal Training</p>
        <p class="promo__web">www.fitlane-studio.com.au</p>
      </div>
    </div>
  </section>

</main>
</body>
</html>
```